Probate (Legal) Wordpress Design with Coding for Online Company

I need a Wordpress design with coding, pictures, content to be provided by me, fully responsive, and development. This is for a 6-7 page design.

Pages Needed: Home/About/Probate/Process/FAQ/Contact Us/Blog.

The home page should be organized as followed:
-Steps in Probate: Gather; Implement; Close (each step will come with content)
-Flat-Fee Price & Savings: Content will go here with a button to contact us (phone number) or just the phone number.
-You Have Questions, We Have Answers: five questions with content. Only one question answer to show at a time when clicked on the question from the list.
-Get to Know Us: a brief description with content about what we do and who we are.

Main image slogan: Helping Californians deal with loss with DIGNITY & UNDERSTATING (you may use a better slogan if you wish).

The Contact page should not have a map since we are an online company. We service the entire state of California in every county and city.

The About page should be simple, direct, and easy on the eye. It should have a brief description of who we are and it should have no more than 6 reasons why the client should hire us.

About our online California company. We are not attorneys but legal document assistants who prepare legal documents for probate estate when someone dies with or without a will and assets need to be distributed. We have a flat-fee for Formal Probate of $999 and $699 for Informal Probate. We are an online company and offer our services to the entire state of California in every county. We do everything over the phone and email. The turn around time for us to prepare the initial legal paperwork for the client is within 3-5 business days. We can prepare, file, serve and manage a probate matter from petition to closing. We are not attorneys so our prices are very affordable compare to the attorney.

The company name for the website will be www.thelarkwellgroup.com, The Larkwell Group.

I do not have a logo yet. The colors of the website should be easy on the eye and calming. THE SITE SHOULD BE SIMPLE AND STRAIGHT TO THE POINT. EASY TO NAVIGATE.

The company phone number should be very visible and should stand out to the client. It should also be clickable and ready to dial for smartphone users.

I do not want a contact form on the homepage. THE MAIN THING IS FOR THE POTENTIAL CLIENT TO CALL OUR OFFICE TO SIGN UP.

I do like some images of family or people since we are dealing with people who just lost a loved one. Not all the images have to be of people.

The site should not look like we practice law or that people can mistake us for attorneys.

Target Market(s)

People who just lost a loved one who had property, assets, in California but died with or without a will or trust. This is for people looking to hire non-attorneys.

Coding

Coded - Design and coding required

Font styles to use
Serif

Colors

Designer to choose colors to be used in the design.

Requirements
Must have
• Refer to Project Description.
Nice to have
• The sample images provided is what I am attracted to for the homepage image.
Should not have

```html
<!DOCTYPE html>
<html lang="en">
<head>
<meta charset="utf-8">
<title>The Larkwell Group — Home</title>
<link rel="stylesheet" href="https://fonts.googleapis.com/css2?family=Crimson+Text:wght@400;600;700&family=Oswald:wght@400;500&family=Open+Sans:wght@400;600;700&display=swap">
<style>
:root{
  --teal:#10677f;
  --teal-dark:#0b5569;
  --orange:#f47b16;
  --ink:#333;
  --muted:#666;
  --pale:#edf7fb;
  --hero-bg:#e4e4e4;
  --white:#fff;
}
*{box-sizing:border-box;margin:0;padding:0}
html,body{width:1200px;height:3358px;overflow:hidden;background:var(--white)}
body{font-family:"Open Sans",Arial,sans-serif;color:var(--ink);position:relative}
.abs{position:absolute}
.serif{font-family:"Crimson Text",Georgia,serif}

/* header */
.topline{left:0;top:0;width:1200px;height:5px;background:var(--orange)}
.call-tab{left:795px;top:0;width:295px;height:42px;background:var(--orange);border-radius:0 0 22px 22px;color:var(--white);font-weight:700;font-size:16px;display:flex;align-items:center;justify-content:center;gap:10px}
.brand{left:99px;top:58px;display:flex;align-items:center;gap:10px}
.brand-dot{width:22px;height:22px;border-radius:50%;background:var(--orange)}
.brand-name{font-family:"Crimson Text",Georgia,serif;font-weight:700;font-size:22px;color:var(--teal);letter-spacing:.5px}
.nav{top:78px;left:457px;display:flex;gap:0;font-size:15px;font-weight:600;color:#111}
.nav span{position:absolute;white-space:nowrap}
.header-rule{left:0;top:126px;width:1200px;height:2px;background:#e7e7e7}

/* hero */
.hero{left:0;top:128px;width:1200px;height:519px;background:linear-gradient(90deg,#dcdcdc,#e8e8e8 45%,#d9d5d2)}
.hero-photo{left:500px;top:128px;width:700px;height:519px;background:linear-gradient(100deg,rgba(232,232,232,0) 0%,#e6c9b8 22%,#d8506a 40%,#e6b393 58%,#e39a3a 78%,#c9a07a 100%)}
.hero-rule{left:99px;width:438px;height:2px;background:var(--orange)}
.hero-title{left:99px;top:218px;font-family:"Crimson Text",Georgia,serif;font-size:52px;color:var(--orange);letter-spacing:1px}
.hero-sub{left:99px;top:336px;font-family:"Oswald",sans-serif;font-size:25px;line-height:40px;color:var(--teal);text-transform:uppercase;font-weight:500}
.btn-outline{display:flex;align-items:center;justify-content:center;font-size:15px;border:2px solid currentColor}
.hero-btn{left:99px;top:448px;width:114px;height:52px;color:#222;border-color:#333}
.arrow{top:355px}

/* about band */
.about-band{left:0;top:647px;width:1200px;height:250px}
.about-title{top:682px;left:0;width:1200px;text-align:center;font-family:"Crimson Text",Georgia,serif;font-size:32px;color:var(--white);font-weight:600}
.about-text{top:755px;left:110px;width:980px;text-align:center;font-size:14px;line-height:23px;color:var(--white);font-weight:600}

/* section titles */
.sec-title{left:0;width:1200px;text-align:center;font-family:"Crimson Text",Georgia,serif;font-size:35px;font-weight:600;color:var(--teal)}
.sec-rule{left:566px;width:68px;height:2px;background:var(--teal)}

/* how it works */
.step-title{font-family:"Crimson Text",Georgia,serif;font-size:28px;font-weight:600}
.step-text{font-size:14px;line-height:23px;color:var(--muted);width:320px}
.badge{width:54px;height:54px;border-radius:50%;color:var(--white);font-size:26px;display:flex;align-items:center;justify-content:center}

/* flat fee */
.fee-band{left:0;top:1623px;width:1200px;height:374px;background:var(--pale)}
.fee-photo{left:0;top:1623px;width:520px;height:374px;background:radial-gradient(ellipse at 52% 58%,#d45b86 0%,#e9a8bf 22%,#f0dcd4 42%,rgba(237,247,251,0) 70%)}
.fee-title{left:544px;top:1662px;font-family:"Crimson Text",Georgia,serif;font-size:36px;font-weight:600;color:var(--teal)}
.fee-text{left:544px;top:1735px;width:620px;font-size:14px;line-height:23px;color:var(--muted)}
.btn-solid{display:flex;align-items:center;justify-content:center;background:var(--orange);color:var(--white);font-size:14px;font-weight:600}
.fee-btn{left:544px;top:1867px;width:116px;height:54px}

/* faq */
.faq-tab{left:99px;width:405px;height:48px;border:2px solid var(--teal);border-radius:24px;display:flex;align-items:center;padding-left:20px;font-size:15px;color:var(--teal)}
.faq-tab.active{background:var(--orange);border-color:var(--orange);color:var(--white);border-radius:24px 0 0 24px}
.faq-q{left:549px;top:2196px;font-size:17px;font-weight:700;color:var(--teal)}
.faq-a{left:549px;top:2243px;width:560px;font-size:14px;line-height:23px;color:var(--muted)}
.faq-list{left:549px;top:2343px;list-style:none;font-size:14px;font-weight:600;color:#222}
.faq-list li{height:31px;display:flex;align-items:center;gap:14px}

/* get to know us */
.know{top:2588px;width:600px;height:489px}
.know-do{left:0;background:linear-gradient(135deg,#1a86a5,#136e88 55%,#0f5f78)}
.know-who{left:600px;background:linear-gradient(135deg,#c47a1e,#b56d17 55%,#9c5e14)}
.know-title{font-family:"Crimson Text",Georgia,serif;font-size:33px;color:var(--white);letter-spacing:.5px}
.know-rule{width:102px;height:2px;background:var(--white)}
.know-text{width:480px;font-size:14px;line-height:24px;color:var(--white);font-weight:600}
.know-btn{width:114px;height:52px;color:var(--white)}

/* footer */
.foot-nav{top:3147px;left:0;width:1200px;display:flex;justify-content:center;gap:26px;font-size:15px;color:#111}
.contact-row{top:3222px;display:flex;align-items:center;gap:14px;font-size:21px;color:#222}
.icon-ring{width:44px;height:44px;border:2px solid #222;border-radius:50%;display:flex;align-items:center;justify-content:center}
.foot-rule{left:99px;top:3302px;width:1002px;height:2px;background:#222}
.copyright{top:3325px;left:0;width:1200px;text-align:center;font-size:15px;color:#222}
</style>
</head>
<body>

<!-- header -->
<div class="abs topline"></div>
<div class="abs call-tab">
  <svg width="16" height="16" viewBox="0 0 24 24" fill="#fff"><path d="M6.6 10.8a15.1 15.1 0 0 0 6.6 6.6l2.2-2.2a1 1 0 0 1 1-.25 11.4 11.4 0 0 0 3.6.6 1 1 0 0 1 1 1V20a1 1 0 0 1-1 1A17 17 0 0 1 3 4a1 1 0 0 1 1-1h3.5a1 1 0 0 1 1 1c0 1.25.2 2.45.6 3.6a1 1 0 0 1-.25 1z"/></svg>
  Call Us At: +180 025 7410
</div>
<div class="abs brand"><span class="brand-dot"></span><span class="brand-name">THE LARKWELL GROUP</span></div>
<nav class="abs nav" style="left:0;width:1200px">
  <span style="left:457px">HOME</span>
  <span style="left:544px">ABOUT</span>
  <span style="left:636px">PROBATE</span>
  <span style="left:746px">PROCESS</span>
  <span style="left:853px">FAQ</span>
  <span style="left:922px">CONTACT US</span>
  <span style="left:1057px">BLOG</span>
</nav>
<div class="abs header-rule"></div>

<!-- hero -->
<section class="abs hero"></section>
<div class="abs hero-photo" role="img" aria-label="Photo of a smiling mother comforting her two young children"></div>
<div class="abs hero-rule" style="top:204px"></div>
<h1 class="abs hero-title">THE LARKWELL GROUP</h1>
<div class="abs hero-rule" style="top:302px"></div>
<p class="abs hero-sub">Helping Californians deal with loss with<br>dignity &amp; understanding</p>
<a class="abs btn-outline hero-btn">READ MORE</a>
<svg class="abs arrow" style="left:30px" width="30" height="60" viewBox="0 0 30 60"><polyline points="26,2 4,30 26,58" fill="none" stroke="#555" stroke-width="2"/></svg>
<svg class="abs arrow" style="left:1140px" width="30" height="60" viewBox="0 0 30 60"><polyline points="4,2 26,30 4,58" fill="none" stroke="#555" stroke-width="2"/></svg>

<!-- about probate -->
<svg class="abs about-band" viewBox="0 0 1200 250" width="1200" height="250">
  <polygon points="0,0 1200,0 1200,175 600,250 0,175" fill="var(--teal)"/>
  <polyline points="6,0 6,170 600,243 1194,170 1194,0" fill="none" stroke="#fff" stroke-opacity=".55" stroke-width="1.5"/>
  <polyline points="592,212 600,219 608,212" fill="none" stroke="#fff" stroke-width="2"/>
  <polyline points="592,219 600,226 608,219" fill="none" stroke="#fff" stroke-width="2"/>
</svg>
<h2 class="abs about-title">ABOUT PROBATE</h2>
<p class="abs about-text">We are not attorneys but legal document assistants who prepare legal documents for probate estate when someone dies with or without a will and assets need to be distributed. We have a flat-fee for Formal Probate of $999 and $699 for Informal Probate. We are an online company and offer our services to the entire state of California in every county.</p>

<!-- how it works -->
<h2 class="abs sec-title" style="top:948px">HOW IT WORKS</h2>
<div class="abs sec-rule" style="top:1014px"></div>
<svg class="abs" style="left:440px;top:1076px" width="320" height="320" viewBox="0 0 320 320">
  <circle cx="160" cy="160" r="148" fill="none" stroke="#444" stroke-width="3"/>
  <path d="M160 12 A148 148 0 0 1 281 75" fill="none" stroke="var(--teal)" stroke-width="4"/>
  <path d="M39 75 A148 148 0 0 1 160 12" fill="none" stroke="var(--orange)" stroke-width="4"/>
  <path d="M12 160 A148 148 0 0 1 39 75" fill="none" stroke="var(--orange)" stroke-width="4"/>
</svg>
<div class="abs badge" style="left:694px;top:1129px;background:var(--teal)">1</div>
<div class="abs badge" style="left:443px;top:1129px;background:var(--orange)">3</div>
<div class="abs badge" style="left:573px;top:1344px;background:#444">2</div>

<h3 class="abs step-title" style="left:790px;top:1106px;color:var(--teal)">Gather:</h3>
<p class="abs step-text" style="left:790px;top:1154px">Duis aute irure dolor in reprehenderit in vo luptate velit esse cillum dolore eu fugiat nulla pariatur.</p>
<h3 class="abs step-title" style="left:88px;top:1106px;width:320px;text-align:right;color:var(--orange)">Close:</h3>
<p class="abs step-text" style="left:88px;top:1154px;text-align:right">Duis aute irure dolor in reprehenderit in vo luptate velit esse cillum dolore eu fugiat nulla pariatur.</p>
<h3 class="abs step-title" style="left:440px;top:1424px;width:320px;text-align:center;color:#444">Implement:</h3>
<p class="abs step-text" style="left:440px;top:1475px;text-align:center">Duis aute irure dolor in reprehenderit in vo luptate velit esse cillum dolore eu fugiat nulla pariatur.</p>

<!-- flat fee -->
<section class="abs fee-band"></section>
<div class="abs fee-photo" role="img" aria-label="Photo of cupped hands protecting a pink piggy bank"></div>
<h2 class="abs fee-title">Flat-Fee Price &amp; Savings:</h2>
<p class="abs fee-text">Nemo enim ipsam voluptatem quia voluptas sit aspernatur aut odit aut fugit, sed quia consequuntur magni dolores eos qui ratione voluptatem sequi nesciunt. Neque porro quisquam est, qui dolorem ipsum quia dolor sit amet, consectetur, adipisci velit, sed quia non numquam.</p>
<a class="abs btn-solid fee-btn">CONTACT US</a>

<!-- faq -->
<h2 class="abs sec-title" style="top:2044px">OUR FAQ</h2>
<div class="abs sec-rule" style="top:2108px"></div>
<div class="abs faq-tab active" style="top:2188px">Nemo enim ipsam voluptatem quia voluptas?</div>
<svg class="abs" style="left:502px;top:2188px" width="22" height="48" viewBox="0 0 22 48"><polygon points="0,0 22,24 0,48" fill="var(--orange)"/></svg>
<div class="abs faq-tab" style="top:2248px">Magni dolores eos qui ratione voluptatem?</div>
<div class="abs faq-tab" style="top:2308px">Sed ut perspiciatis unde omnis natus?</div>
<div class="abs faq-tab" style="top:2368px">Enim ad minima veniam, quis nostrum?</div>
<div class="abs faq-tab" style="top:2428px">Quis autem vel eum iure reprehenderit?</div>
<h3 class="abs faq-q">NEMO ENIM IPSAM VOLUPTATEM:</h3>
<p class="abs faq-a">Sed ut perspiciatis unde omnis iste natus error sit voluptatem accusantium dolorem que laudantium, totam rem aperiam, eaque ipsa quae ab illo inventore veritatis et quasi architecto beatae vitae dicta sunt explicabo.</p>
<ul class="abs faq-list">
  <li><svg width="14" height="12" viewBox="0 0 14 12"><path d="M1 6h9M6 1l6 5-6 5" fill="none" stroke="var(--orange)" stroke-width="2"/></svg>Sed ut perspiciatis unde omnis iste natus error sit voluptate.</li>
  <li><svg width="14" height="12" viewBox="0 0 14 12"><path d="M1 6h9M6 1l6 5-6 5" fill="none" stroke="var(--orange)" stroke-width="2"/></svg>Accusantium dolorem que laudantium, totam rem.</li>
  <li><svg width="14" height="12" viewBox="0 0 14 12"><path d="M1 6h9M6 1l6 5-6 5" fill="none" stroke="var(--orange)" stroke-width="2"/></svg>Aperiam, eaque ipsa quae ab illo inventore veritatis.</li>
  <li><svg width="14" height="12" viewBox="0 0 14 12"><path d="M1 6h9M6 1l6 5-6 5" fill="none" stroke="var(--orange)" stroke-width="2"/></svg>Quasi architecto beatae vitae dicta sunt explicabo.</li>
</ul>

<!-- what we do / who we are -->
<section class="abs know know-do" role="img" aria-label="Teal-tinted photo of a person working at a desk"></section>
<section class="abs know know-who" role="img" aria-label="Orange-tinted photo of hands writing on paperwork"></section>

<h2 class="abs know-title" style="left:99px;top:2642px">WHAT WE DO</h2>
<div class="abs know-rule" style="left:99px;top:2706px"></div>
<p class="abs know-text" style="left:99px;top:2740px">Sed ut perspiciatis unde omnis iste natus error sit voluptatem accu santium doloremque laudantium, totam rem aperiam, eaque ipsa quae ab illo inventore veritatis et quasi architecto beatae.</p>
<p class="abs know-text" style="left:99px;top:2836px">Nemo enim ipsam voluptatem quia voluptas sit aspernatur aut odit aut fugit, sed quia consequuntur magni dolores eos qui ratione vo luptatem.</p>
<a class="abs btn-outline know-btn" style="left:99px;top:2946px">READ MORE</a>

<h2 class="abs know-title" style="left:634px;top:2642px">WHO WE ARE</h2>
<div class="abs know-rule" style="left:634px;top:2706px"></div>
<p class="abs know-text" style="left:634px;top:2740px">Sed ut perspiciatis unde omnis iste natus error sit voluptatem accu santium doloremque laudantium, totam rem aperiam, eaque ipsa quae ab illo inventore veritatis et quasi architecto beatae.</p>
<p class="abs know-text" style="left:634px;top:2836px">Nemo enim ipsam voluptatem quia voluptas sit aspernatur aut odit aut fugit, sed quia consequuntur magni dolores eos qui ratione vo luptatem.</p>
<a class="abs btn-outline know-btn" style="left:634px;top:2946px">READ MORE</a>

<!-- footer -->
<nav class="abs foot-nav">
  <span>HOME</span><span>|</span><span>ABOUT</span><span>|</span><span>PROBATE</span><span>|</span><span>PROCESS</span><span>|</span><span>FAQ</span><span>|</span><span>CONTACT US</span><span>|</span><span>BLOG</span>
</nav>
<div class="abs contact-row" style="left:101px">
  <span class="icon-ring"><svg width="20" height="20" viewBox="0 0 24 24" fill="#222"><path d="M6.6 10.8a15.1 15.1 0 0 0 6.6 6.6l2.2-2.2a1 1 0 0 1 1-.25 11.4 11.4 0 0 0 3.6.6 1 1 0 0 1 1 1V20a1 1 0 0 1-1 1A17 17 0 0 1 3 4a1 1 0 0 1 1-1h3.5a1 1 0 0 1 1 1c0 1.25.2 2.45.6 3.6a1 1 0 0 1-.25 1z"/></svg></span>
  +180 025 7410
</div>
<div class="abs contact-row" style="left:343px">
  <span class="icon-ring"><svg width="22" height="16" viewBox="0 0 22 16"><rect x="1" y="1" width="20" height="14" rx="2" fill="none" stroke="#222" stroke-width="2"/><polyline points="1,2 11,9 21,2" fill="none" stroke="#222" stroke-width="2"/></svg></span>
  info@thelarkwellgroup.com
</div>
<div class="abs contact-row" style="left:678px">
  <span class="icon-ring"><svg width="16" height="22" viewBox="0 0 16 22"><path d="M8 21s7-8 7-13A7 7 0 0 0 1 8c0 5 7 13 7 13z" fill="none" stroke="#222" stroke-width="2"/><circle cx="8" cy="8" r="2.5" fill="#222"/></svg></span>
  456 Harbor Lane, Suite 210, CA 902
</div>
<div class="abs foot-rule"></div>
<p class="abs copyright">Copyrights @ 2017 The Larkwell Group. All Rights Reserved.</p>

</body>
</html>
```